Wordpress Website for Waikiki based Boutique Retail Commercial Realestate Company

Aloha!
We need a wordpress design for a new company based in Waikiki, Oahu. I am an experienced real estate professional leaving a large national firm to open a boutique agency. I have several colleagues that work for these type of boutique companies on the mainland - and all seemingly have similar type Wordpress websites. Below are the examples I'd like you to use as a starting point but I would like to differentiate ourselves because of our unique position of being located on a tropical island. The design should communicate elegance, sophistication, experience and market knowledge. The photos should all be of Hawaii and Waikiki.

Here are the websites I'd like this to be similar to (but smaller since I am currently a one woman company):
http://www.plv.example/
http://marlowegroupe.example/
http://www.brannockco.example/
(this one is residential real estate, which I don't do but still like this look): http://www.coraldwell.example/

I am not that tech savy but I do own my domain, have it hosted and have had the hosting company install the necessary Wordpress component on to the account.

I would like to form a relationship with a designer that can grow with me so as I want to add features in the future, I can continue to hire you. If you are strictly a designer, that is ok, but I am also looking for someone to do regular administrative work on the website by uploading new information to it regularly.

Also, would you advise me on how to "upload" it to the hosting company?

Aloha Designers,

Here are examples of the interactive map that I'd like to do for my living resume. Instead of an image, however, I'd like it to be over an aerial from Google Earth of Waikiki:

http://www.grandlagoonarcade.example/
http://www.shorelinepromenade.example/

Hope this answers some questions. I look forward to your designs! Mahalo, Marielle

Target Market(s)

upscale & luxury retailers as well as owners of property in Waikiki

Industry/Entity Type

Real Estate

Requirements
Must have
• I need to have the web page coded so I can upload and have a working live web page.

Here is the unique element I'd like to have on my webpage:

I'd like to have a map of Waikiki (Google earth image) that has roll-overs on it. This will be my living, breathing resume. So when someone visits my website, they can roll-over the map and the name of a property will pop-up. They can expand on it to learn more about the work I've done on that property. Don't worry, I'll provide you will all the detail but I'd like to see a sample of how you would handle this.

The only design idea that I've had or thought to play with would be to have the website all in shades of grey except for whatever is being featured - so if there is a large photo - everything would be grey except for the subject building. I don't know if there is an easy Photoshop or software way to do this, and if not, then skip the idea because it would be too labor intensive for lots of photos.

Below is all the typical pages a company like me would have:
Landing Page - full photo images
Assignments/Listings Page
Services Page - this page might have the map described above
News Page
(I'd like to be able to either have this connect to RSS/Twitter/FB. I basically want to take local news articles and upload them here. I will also have an admin person email blast these to my clients once a week in the future. I need some capture system here for people to sign up to receive the news by email, sign up to receive available listings or sign up to participate in future surveys of Waikiki- I'm about to launch one in a week or two).

Contact Page
Nice to have
• Client Access Only Page-
With this page, I'd like to have the ability to control who has access to this page.

It should require their email and password.
It should show the files in PDF format (like the link below)
It should allow them to download the file.
It should send me an email every time someone access this Client Page.

http://www.kelvanorshops.example/catalog-leasing-2011.html

```html
<!DOCTYPE html>
<html lang="en">
<head>
<meta charset="utf-8">
<title>Lanai Marsh &amp; Co — Retail Real Estate, Waikiki</title>
<link rel="stylesheet" href="https://fonts.googleapis.com/css2?family=PT+Sans+Narrow:wght@400;700&family=PT+Sans:wght@400;700&display=swap">
<style>
:root{
  --sky-top:#3f7fc4;
  --sky-mid:#8fb8de;
  --city:#c9c4b6;
  --sea:#3aa0b8;
  --sand:#d9c7a4;
  --bar-top:#3a3a3a;
  --bar-bottom:#050505;
  --nav-text:#b9b9b9;
  --nav-active:#2c5f9c;
  --accent-blue:#2f74bd;
  --panel:#f4f4f4;
  --panel-edge:#d6d6d6;
  --label-grey:#6b6b6b;
  --footer:#3b3b3b;
  --footer-text:#eeeeee;
  --white:#ffffff;
}
*{box-sizing:border-box;margin:0;padding:0}
html,body{width:1200px;height:966px;overflow:hidden}
body{position:relative;font-family:"PT Sans",sans-serif;background:var(--footer)}
.hero-photo{position:absolute;left:0;top:0;width:1200px;height:890px;
  background:linear-gradient(180deg,var(--sky-top) 0%,var(--sky-mid) 38%,var(--city) 58%,var(--sea) 74%,var(--sand) 100%)}
.header-bar{position:absolute;left:292px;top:38px;width:831px;height:97px;border-radius:0 10px 10px 0;
  background:linear-gradient(180deg,var(--bar-top),var(--bar-bottom) 60%);box-shadow:0 2px 4px rgba(0,0,0,.4)}
.brand{position:absolute;left:85px;top:0;width:208px;height:206px;border-radius:0 0 8px 8px;
  background:linear-gradient(180deg,#2b2b2b,#0a0a0a 75%,#3a3a3a);box-shadow:0 2px 6px rgba(0,0,0,.5);
  display:flex;flex-direction:column;align-items:center;justify-content:center;gap:14px}
.brand-mark{width:46px;height:46px;border:3px solid #cfcfcf}
.brand-name{font-family:"PT Sans",sans-serif;color:#cfcfcf;font-size:24px;text-align:center;line-height:1.1}
.main-nav{position:absolute;top:38px;left:492px;display:flex;font-family:"PT Sans Narrow",sans-serif;font-weight:700;font-size:18px}
.main-nav a{color:var(--nav-text);text-decoration:none;height:52px;line-height:56px;padding:0 18px;text-transform:uppercase}
.main-nav a.active{background:linear-gradient(180deg,#3b78bb,var(--nav-active));color:var(--white);border-radius:0 0 8px 8px;padding:0 17px 0 21px}
.search{position:absolute;left:918px;top:99px;width:170px;height:25px;background:var(--white);border:1px solid #999;
  font-size:12px;font-style:italic;color:#a7a7a7;padding:4px 12px}
.search svg{position:absolute;right:6px;top:6px}
.search-tab{position:absolute;left:877px;top:288px;width:250px;height:70px;background:var(--panel);border-radius:8px 8px 0 0;border:1px solid var(--panel-edge);border-bottom:none}
.search-tab h2{font-family:"PT Sans Narrow",sans-serif;font-size:18px;color:var(--label-grey);margin:12px 0 0 31px;text-transform:uppercase}
.search-tab p{font-family:"PT Sans Narrow",sans-serif;font-weight:700;font-size:13px;color:var(--accent-blue);margin:8px 0 0 31px}
.featured{position:absolute;left:449px;top:344px;width:678px;height:316px;background:linear-gradient(180deg,var(--panel),#e2e2e2);
  border:1px solid var(--panel-edge);border-radius:8px 0 8px 8px;box-shadow:0 3px 6px rgba(0,0,0,.25)}
.featured h2{position:absolute;left:36px;top:14px;font-family:"PT Sans Narrow",sans-serif;font-size:18px;color:var(--label-grey);text-transform:uppercase}
.pager{position:absolute;right:18px;top:10px;font-size:24px;color:#888;letter-spacing:8px}
.card{position:absolute;top:48px;width:189px;height:240px;background:var(--white);border:1px solid #ddd;border-radius:3px}
.card .thumb{position:absolute;left:9px;top:9px;width:170px;height:170px;border-radius:4px}
.card h3{position:absolute;left:17px;top:187px;font-family:"PT Sans Narrow",sans-serif;font-size:15px;color:var(--label-grey);text-transform:uppercase;font-weight:400}
.card p{position:absolute;left:17px;top:211px;font-family:"PT Sans Narrow",sans-serif;font-weight:700;font-size:15px;color:var(--accent-blue);text-transform:uppercase}
.slide-arrow{position:absolute;top:411px}
.tagline{position:absolute;right:82px;top:686px;text-align:right;color:var(--white);text-shadow:1px 2px 3px rgba(0,0,0,.6);text-transform:uppercase;font-family:"PT Sans",sans-serif}
.tagline .line1{font-size:30px;letter-spacing:-.5px}
.tagline .line1 b{font-size:46px;font-weight:400}
.tagline .line2{font-size:30px;margin-top:8px;display:block}
.site-footer{position:absolute;left:0;top:890px;width:1200px;height:76px;background:var(--footer)}
.social{position:absolute;left:109px;top:25px;display:flex;gap:6px}
.social span{width:20px;height:20px;border-radius:3px;background:#8a8a8a}
.legal{position:absolute;right:90px;top:10px;font-size:12px;color:var(--footer-text);text-align:right;line-height:24px}
.legal a{color:var(--footer-text);text-decoration:none}
</style>
</head>
<body>
<div class="hero-photo" role="img" aria-label="Photo of Waikiki beach with hotel towers, palm trees, a yellow catamaran, surfboards and swimmers in the sea"></div>

<div class="header-bar"></div>
<div class="brand"><span class="brand-mark"></span><span class="brand-name">Lanai Marsh<br>&amp; Co</span></div>
<nav class="main-nav">
  <a class="active" href="#">Home</a><a href="#">About Us</a><a href="#">Listings</a><a href="#">Services</a><a href="#">Clients</a><a href="#">News</a><a href="#">Contact</a>
</nav>
<div class="search">Search
  <svg width="12" height="12" viewBox="0 0 12 12"><circle cx="5" cy="5" r="3.5" fill="none" stroke="#aaa" stroke-width="1.4"/><line x1="7.5" y1="7.5" x2="11" y2="11" stroke="#aaa" stroke-width="1.6"/></svg>
</div>

<div class="search-tab"><h2>Search All Listings</h2><p>FOR LEASE | FOR SALE</p></div>

<section class="featured">
  <h2>Featured Listings</h2>
  <div class="pager">❮❯</div>
  <article class="card" style="left:35px">
    <div class="thumb" role="img" aria-label="Balcony view over Waikiki towers" style="background:linear-gradient(180deg,#6fa4d8,#a9b7b9 55%,#6f7f6c)"></div>
    <h3>236 Broadway</h3><p>Waikiki</p>
  </article>
  <article class="card" style="left:246px">
    <div class="thumb" role="img" aria-label="Beachfront with palm trees and a hotel" style="background:linear-gradient(180deg,#5b8fd0,#9ab8e0 55%,#d8c6a4)"></div>
    <h3>Beach Place</h3><p>Oahu Islands</p>
  </article>
  <article class="card" style="left:457px">
    <div class="thumb" role="img" aria-label="Hotel pool deck with palms and umbrellas" style="background:linear-gradient(180deg,#7fb0e0,#c9c1a0 55%,#4fb2d6)"></div>
    <h3>569 &nbsp;West Sunset</h3><p>Waikiki</p>
  </article>
</section>

<svg class="slide-arrow" style="left:10px" width="36" height="36" viewBox="0 0 36 36"><circle cx="18" cy="18" r="17" fill="#eee" stroke="#999"/><path d="M21 10l-8 8 8 8" fill="none" stroke="#444" stroke-width="3.5"/></svg>
<svg class="slide-arrow" style="left:1148px" width="36" height="36" viewBox="0 0 36 36"><circle cx="18" cy="18" r="17" fill="#eee" stroke="#999"/><path d="M15 10l8 8-8 8" fill="none" stroke="#444" stroke-width="3.5"/></svg>

<div class="tagline"><span class="line1">Transforming the <b>Retail</b></span><span class="line2">Landscape</span></div>

<footer class="site-footer">
  <div class="social" aria-label="Social links"><span></span><span></span><span></span><span></span></div>
  <div class="legal">
    <a href="#">Legal</a> &nbsp;| &nbsp;<a href="#">Disclaimer</a> &nbsp;| &nbsp;<a href="#">Privacy Policy</a><br>
    Copyright © &nbsp;2013 &nbsp;harborlinestudio. All rights reserved.
  </div>
</footer>
</body>
</html>
```